依頼詳細
昨年度2月と今年度9月の合同会社説明会のチラシを添付しております。
参考にしてください。
就職活動応援セミナーのテーマと時間は変更になる場合があります。修正要望をさせて頂くこともありますのでご了承ください。
記載項目
チラシに載せていただきたい内容(仕様書)は添付しておりますのでご確認よろしくお願い致します。
サイズ
A4
ページ数
片面
希望イメージ
シンプル 複雑
単色 カラフル
暗い 明るい
日常 高級
遊び心 厳粛
未来的 伝統的
女性的 男性的
希望する色
暖色系でお願いします。
納品ファイル
• イラストレーター形式 (.ai)
補足説明
納品ファイルは、イラストレーター形式Ver10以下でお願いします。

選択させて頂いたデザインの著作権(財産権)等の扱いはPikuros利用規約に従い、弊社に譲渡をお願いします。フォントや画像素材などを利用する場合は上記利用用途に使用できることを確認し、第三者の知的財産権等に注意して下さい。

以下は、現在のウェブサイトです。
http://www.mn-jobsupport.jp/

よろしくお願いいたします。
就職活動応援セミナーのテーマと時間が変更になりましたのでお知らせいたします。
テーマ「就職活動の落し穴」
時間「12:15~12:50」
です。仕様書も添付しております。
変更箇所は赤字にしております。
お手数をおかけしますがよろしくお願い致します。
■ 選んだ理由

合同会社説明会の情報が分かりやすかったので
選ばせていただきました。
細かい修正もしていただいて本当にありがとうございました。

■ 提案者全員のお礼・コメント

提案してくださった皆様、本当にありがとうございました。
話し合いの結果、一つの提案に決定しましたが、
どれもすばらしくてとても迷いました。
お忙しい中、チラシを作成していただきありがとうございました。

```html
<!DOCTYPE html>
<html lang="ja">
<head>
<meta charset="utf-8">
<title>新生活産業 合同会社説明会</title>
<link rel="stylesheet" href="https://fonts.googleapis.com/css2?family=Noto+Sans+JP:wght@400;500;700;900&family=Oswald:wght@500;700&display=swap">
<style>
:root{
  --red:#d7262b;
  --red-dark:#b3151c;
  --orange:#e96b1f;
  --blue:#1f5fa8;
  --ink:#333333;
  --line:#d4d4d4;
  --white:#ffffff;
}
*{margin:0;padding:0;box-sizing:border-box}
html,body{width:846px;height:1200px;overflow:hidden;background:var(--white)}
body{font-family:"Noto Sans JP",sans-serif;color:var(--ink)}
.flyer{position:relative;width:846px;height:1200px;overflow:hidden;
  background:repeating-linear-gradient(180deg,#fff 0 46px,#f6f6f6 46px 92px)}
.hero{position:absolute;left:0;top:0;width:846px;height:335px;
  background:linear-gradient(180deg,#cfe0f1 0%,#eef4fa 70%,#ffffff 100%)}
.badge{position:absolute;left:716px;top:290px;width:110px;height:110px;border-radius:50%;
  background:var(--red);color:var(--white);text-align:center;border:4px solid var(--white);
  box-shadow:0 0 0 2px var(--red)}
.badge .num{display:block;font-family:"Oswald",sans-serif;font-weight:700;font-size:42px;line-height:1;margin-top:20px}
.badge .num small{font-family:"Noto Sans JP",sans-serif;font-size:24px}
.badge .cap{display:block;font-size:12px;font-weight:700;margin-top:4px}
.ribbon{position:absolute;left:323px;top:346px;width:200px;height:30px;background:var(--blue);
  color:var(--white);font-weight:700;font-size:19px;text-align:center;line-height:30px;letter-spacing:2px}
.title{position:absolute;left:0;top:376px;width:846px;text-align:center;font-weight:900;
  font-size:74px;letter-spacing:4px;color:var(--red-dark);line-height:1.05}
.lead{position:absolute;left:62px;top:478px;width:430px;font-size:13.5px;line-height:1.7}
.perks{position:absolute;left:520px;top:478px;width:270px;display:grid;grid-template-columns:1fr 1fr;gap:8px}
.perk{height:30px;border-radius:5px;background:var(--red);color:var(--white);font-weight:700;
  font-size:16px;text-align:center;line-height:30px}
.date{position:absolute;left:62px;top:572px;color:var(--red);font-family:"Oswald",sans-serif;font-weight:700;
  font-size:92px;line-height:1;display:flex;align-items:flex-end}
.date .jp{font-family:"Noto Sans JP",sans-serif;font-weight:900;font-size:60px;margin:0 2px 6px}
.date .side{display:flex;flex-direction:column;align-items:center;margin:0 0 8px 10px}
.date .year{font-size:24px;color:var(--red)}
.date .dow{width:40px;height:40px;border-radius:50%;background:var(--red);color:var(--white);
  font-family:"Noto Sans JP",sans-serif;font-size:24px;line-height:40px;text-align:center;margin-top:4px}
.time{position:absolute;left:62px;top:680px;font-size:30px;font-weight:700;display:flex;align-items:center;gap:8px;white-space:nowrap}
.time small{font-size:15px;font-weight:500}
.info{position:absolute;left:62px;width:420px;display:flex;gap:12px;align-items:flex-start}
.info .label{flex:none;width:54px;height:54px;border-radius:50%;background:var(--blue);color:var(--white);
  font-size:14px;font-weight:700;text-align:center;line-height:54px}
.info .body{font-size:13px;line-height:1.55;padding-top:4px}
.info .body strong{display:block;font-size:21px;font-weight:900;line-height:1.3;white-space:nowrap}
.info.venue{top:728px}
.info.target{top:796px}
.info.host{top:862px}
.building{position:absolute;left:62px;top:930px;width:420px;height:28px;background:linear-gradient(90deg,#e9eef4,#f8f8f8)}
.seminar{position:absolute;left:500px;top:578px;width:310px;height:196px;background:var(--white);
  border:2px solid var(--red)}
.seminar h2{background:var(--red);color:var(--white);font-size:19px;font-weight:900;text-align:center;height:36px;line-height:36px;letter-spacing:1px}
.seminar .theme{font-size:16px;font-weight:700;text-align:center;margin:8px 0 6px}
.seminar dl{display:grid;grid-template-columns:46px 1fr;gap:5px 8px;margin:0 14px;font-size:13.5px;align-items:center}
.seminar dt{background:var(--orange);color:var(--white);font-size:12px;text-align:center;border-radius:3px;height:20px;line-height:20px}
.seminar .note{margin:8px 10px 0;font-size:12px;color:var(--red);line-height:1.4;text-align:center}
.map{position:absolute;left:500px;top:792px;width:310px;height:166px;border:1px solid var(--line);
  background:linear-gradient(135deg,#f5f5f5,#e6e6e6)}
.map-tag{position:absolute;left:500px;top:792px;background:var(--blue);color:var(--white);font-family:"Oswald",sans-serif;
  font-size:14px;padding:1px 10px}
.footer{position:absolute;left:0;top:976px;width:846px;height:224px;background:var(--blue);color:var(--white)}
.footer .org{position:absolute;left:62px;top:22px;font-size:22px;font-weight:900}
.footer .addr{position:absolute;left:62px;top:58px;font-size:11px;line-height:1.5}
.footer .tel{position:absolute;left:62px;top:92px;font-family:"Oswald",sans-serif;font-size:46px;font-weight:700;display:flex;align-items:baseline;gap:8px}
.footer .tel span{font-size:26px}
.footer .note{position:absolute;left:440px;top:104px;width:270px;font-size:10.5px;line-height:1.5}
.footer .url{position:absolute;left:62px;top:172px;font-size:18px;font-weight:700;letter-spacing:.5px}
</style>
</head>
<body>
<main class="flyer">
  <div class="hero" role="img" aria-label="スーツ姿の若い男女5人の写真が横一列に並ぶ明るい背景"></div>

  <div class="badge"><span class="num">24<small>社</small></span><span class="cap">参加予定企業</span></div>
  <div class="ribbon">新生活産業</div>
  <h1 class="title">合同会社説明会</h1>

  <p class="lead">ライフスタイルの変化に伴いニーズが増加している個人・家庭向けサービス分野の企業を中心とした、24社が一同に会した合同会社説明会です。ぜひご参加下さい。</p>
  <div class="perks">
    <div class="perk">入場無料</div>
    <div class="perk">入退場自由</div>
    <div class="perk">予約不要</div>
    <div class="perk">履歴書不要</div>
  </div>

  <div class="date">1<span class="jp">月</span>31<span class="jp">日</span>
    <span class="side"><span class="year">2012年</span><span class="dow">火</span></span>
  </div>
  <div class="time">
    <svg width="26" height="26" viewBox="0 0 26 26"><circle cx="13" cy="13" r="11" fill="none" stroke="#333" stroke-width="2.5"/><path d="M13 6v7l5 3" fill="none" stroke="#333" stroke-width="2.5" stroke-linecap="round"/></svg>
    13:00～16:30<small>(受付16:00まで)</small>
  </div>

  <div class="info venue"><span class="label">会場</span><div class="body"><strong>みなと中央ビル11階10号会議室</strong>みなと市中央区本町1丁目2番3号</div></div>
  <div class="info target"><span class="label">対象</span><div class="body">求職者および平成24年3月卒業<br>予定者(大学・短大・専修学校等)</div></div>
  <div class="info host"><span class="label">主催</span><div class="body">みなと県・公益社団法人<br>みなと県雇用対策協会</div></div>
  <div class="building" role="img" aria-label="会場ビルの外観イラスト"></div>

  <section class="seminar">
    <h2>就職活動応援セミナー</h2>
    <p class="theme">テーマ「就職活動の落し穴」</p>
    <dl>
      <dt>時間</dt><dd>12:15～12:50</dd>
      <dt>会場</dt><dd>みなと中央ビル11階3号会議室</dd>
      <dt>定員</dt><dd>40名</dd>
    </dl>
    <p class="note">参加ご希望の方は、事前に事務局まで<br>ご連絡下さい。(予約制)</p>
  </section>

  <div class="map" role="img" aria-label="会場周辺の案内地図"></div>
  <span class="map-tag">MAP</span>

  <footer class="footer">
    <p class="org">みなと県新生活産業就職支援事業事務局</p>
    <p class="addr">みなと市中央区本町1-2-3 中央ビル5F<br>受付時間 平日9:00～17:00</p>
    <p class="tel"><span>TEL.</span>092-555-0147</p>
    <p class="note">本事業はみなと県の委託を受け、公益社団法人みなと県雇用対策協会が実施しています。</p>
    <p class="url">http://www.mn-jobsupport.jp/</p>
  </footer>
</main>
</body>
</html>
```